Design the Mobile Version of Existing Web Based Health Platform

Loomcrest is a social business enterprise that focus on public health by applying innovative healthcare services and consumer internet technology. Loomcrest offers a personalized platform of health promotion and disease prevention that puts the individual back in control of his life.

Loomcrest is looking for a Mobile Web UX/Visual Design professional to create a mobile version of Loomcrest website platform for iPhone, iPad/tablet and Android.

Contestants must to check www.loomcrest-demo.com.br to have a better understanding of Loomcrest Platform by creating an account (it's in portuguese, but anyone can get the general idea).

The mobile version of Loomcrest should have very similar functionality and user flows. This job is not to reengineer or re-imagine Loomcrest. It is just to reformat the existing functionality so it works well on mobile devices.

This description below is to help you to understand the core features of the platform (check the attachments to see the new web design of each one):

- Personally Controlled Health Record - PCHR enables an individual to own and manage a complete, secure, digital copy of her health and wellness information.
- Health Risk Assessments - is a process to estimate the nature and probability of adverse health effects, based on personal and family historical data, behavior and environment.
- Simulation of future health - "what if analysis" that emphasizes health education and behavior change.
- Step Quests - a program that gives you the opportunity to the participant to advance his personal well-being by doing simple Step Quests
- Health Alerts and Recommendations and Missing Data - Recommendations based on Wellbeing Bureau Guidelines and Federal Wellness Review Panel (FWRP), plus notifications to update outdated information.

The deliverable for this project is a psd file with a designed mobile version of Loomcrest.

A new design of the web platform is under construction. You can also check it looking at the files attached.

Target Market(s)

people 25-40 years old, 60% female, socially engaged

Industry/Entity Type

Healthcare

Requirements
Must have
• iPhone, iPad and Android version

Design must cover all current functionalities available on the web version (please, ensure you understand all features by creating an account at www.loomcrest-demo.com.br)

- Login/Sign up
- Welcome (first assessment)
- Add to Personal Controlled Health Record (PCHR)
- Update/Remove PCHR
- List PCHR
- Riskgrid (risk assessmen results)
- Simulation
- Alerts
- Missing data
- Recommendations
- StepQuest
- Badges
- Configurations

It's important to check the attachments to see how the web platform design is evolving.

```html
<!DOCTYPE html>
<html lang="pt">
<head>
<meta charset="utf-8">
<title>Loomcrest – Mobile Screens</title>
<link rel="stylesheet" href="https://fonts.googleapis.com/css2?family=Open+Sans:wght@300;400;600;700&display=swap">
<style>
  :root{
    --bg:#2e2e2e;
    --green:#8dc63f;
    --orange:#f7941d;
    --bar:#2f2f2f;
    --ink:#4a4a4a;
    --grey:#8a8a8a;
    --tile:#ececec;
    --field:#ffffff;
    --alert:#e0262f;
    --panel:rgba(120,120,120,.55);
  }
  *{box-sizing:border-box;margin:0;padding:0}
  html,body{width:1200px;height:590px;overflow:hidden;background:var(--bg);font-family:"Open Sans",Arial,sans-serif}
  .stage{display:flex;gap:24px;padding:136px 27px 0}
  .screen{position:relative;width:211px;height:318px;overflow:hidden;background:#fff}
  .backdrop{position:absolute;inset:0;background:linear-gradient(180deg,#fbf4dc 0%,#f3d9c8 35%,#d59ab8 58%,#5d79b4 80%,#263a66 100%)}
  .backdrop.soft{background:linear-gradient(180deg,#f6efe6 0%,#efd8d4 40%,#c9a2c4 65%,#7f95c6 85%,#4a5f92 100%)}

  /* brand */
  .brand{position:absolute;left:0;top:36px;width:100%;text-align:center}
  .brand-name{font-size:28px;font-weight:600;color:var(--ink);line-height:1;letter-spacing:-.3px}
  .brand-tag{font-size:9px;color:#7a7a7a;margin-top:4px}

  /* sign up */
  .signup{position:absolute;left:7px;top:123px;width:197px;height:134px;background:var(--panel);border-radius:3px;padding:5px}
  .social-btn{height:24px;margin-bottom:14px;background:var(--green);color:#fff;font-size:9px;display:flex;align-items:center;justify-content:center}
  .social-btn b{margin-left:3px}
  .field{height:19px;background:var(--field);margin-bottom:8px;font-size:8px;color:var(--ink);padding:4px 5px;line-height:11px}
  .agree{display:flex;height:24px;margin-top:3px}
  .check{width:22px;background:#cfcfcf;display:flex;align-items:center;justify-content:center}
  .terms{width:48px;background:#f2b87a;color:#fff;font-size:7.5px;line-height:1;padding:4px 2px;white-space:nowrap;overflow:hidden}
  .terms small{display:block;font-size:4px;margin-top:2px}
  .cta{flex:1;background:var(--orange);color:#fff;font-size:9px;font-weight:700;display:flex;align-items:center;justify-content:center}

  /* top bar */
  .topbar{position:absolute;left:0;top:0;width:100%;height:26px;background:var(--bar);display:flex;align-items:center;padding:0 4px;z-index:2}
  .back{width:24px;height:16px;background:#e6e6e6;border-radius:2px;display:flex;align-items:center;justify-content:center}
  .user{margin-left:auto;font-size:7px;font-weight:700;color:#fff;margin-right:4px}
  .user span{color:var(--green)}
  .avatar{width:26px;height:22px;background:linear-gradient(#9a9a9a,#555)}
  .badge{width:11px;height:13px;margin-left:3px;background:var(--alert);color:#fff;font-size:8px;font-weight:700;text-align:center;line-height:13px}

  /* menu */
  .tile{position:absolute;width:67px;height:65px;background:var(--tile);border:1px solid #fff;border-radius:4px;box-shadow:0 1px 3px rgba(0,0,0,.35);display:flex;flex-direction:column;align-items:center;justify-content:flex-end;padding-bottom:4px;font-size:7px;font-weight:600;color:#333}
  .tile svg{margin-bottom:4px}
  .settings{position:absolute;right:14px;bottom:8px;font-size:7px;color:#333;display:flex;align-items:center;gap:3px;z-index:1}

  /* records */
  .section{position:absolute;left:0;width:100%;height:30px;display:flex;align-items:center;padding-left:10px;gap:8px;color:#fff;font-size:15px;font-weight:600;z-index:1}
  .section.green{background:var(--green)}
  .section.orange{background:var(--orange)}
  .record{position:absolute;left:7px;width:197px;height:32px;background:rgba(255,255,255,.75);border-radius:2px;display:flex;align-items:center;gap:6px;padding:0 3px;z-index:1}
  .rec-icon{width:33px;height:28px;background:#7d7d7d;display:flex;align-items:center;justify-content:center;color:#fff;font-size:6px;flex-direction:column}
  .rec-value{width:53px;height:24px;background:#fff;border:1px solid #ddd;font-size:16px;font-weight:700;color:#666;display:flex;align-items:center;justify-content:center}
  .rec-value sup{font-size:6px;font-weight:400;line-height:1}
  .rec-date{flex:1;height:24px;background:#fff;border:1px solid #ddd;font-size:8px;color:#666;display:flex;align-items:center;justify-content:center}

  /* risk */
  .blank{position:absolute;left:0;top:29px;width:100%;height:32px;background:#fff;z-index:1}
  .risk-row{position:absolute;left:0;width:100%;display:flex;align-items:center;color:#fff;z-index:1}
  .risk-row .chev{width:14px;text-align:center;font-size:10px;color:#333}
  .risk-main{top:61px;height:61px;background:var(--green);font-size:30px;font-weight:300;gap:12px}
  .risk-map{top:122px;height:34px;background:var(--orange);font-size:13px;gap:10px}
  .risk-reduce{top:157px;height:35px;background:rgba(70,70,70,.85);font-size:13px;gap:10px}
</style>
</head>
<body>
<main class="stage">

  <!-- splash -->
  <section class="screen">
    <div class="backdrop" role="img" aria-label="Soft-focus photo of a dandelion in a pastel meadow"></div>
    <div class="brand">
      <p class="brand-name">Loomcrest</p>
      <p class="brand-tag">Plataforma de Saude Pessoal</p>
    </div>
  </section>

  <!-- sign up -->
  <section class="screen">
    <div class="backdrop" role="img" aria-label="Soft-focus photo of a dandelion in a pastel meadow"></div>
    <div class="brand">
      <p class="brand-name">Loomcrest</p>
      <p class="brand-tag">Plataforma de Saude Pessoal</p>
    </div>
    <form class="signup">
      <div class="social-btn">SING UP WITH <b>FRIENDNET</b></div>
      <div class="field">Email adress...</div>
      <div class="field">Password...</div>
      <div class="field">Rewrite Password...</div>
      <div class="agree">
        <span class="check"><svg width="14" height="12" viewBox="0 0 14 12"><path d="M1 6l4 4 8-9" fill="none" stroke="#fff" stroke-width="2.5"/></svg></span>
        <span class="terms">I accept the<small>terms and conditions</small></span>
        <span class="cta">SING UP</span>
      </div>
    </form>
  </section>

  <!-- menu -->
  <section class="screen">
    <div class="backdrop soft" role="img" aria-label="Blurred pastel meadow photo"></div>
    <header class="topbar">
      <span class="back"><svg width="10" height="8" viewBox="0 0 10 8"><path d="M1 7V1h6M1 1l7 6" stroke="#333" stroke-width="1.6" fill="none"/></svg></span>
      <span class="user">MARCUS <span>DELVANE</span></span>
      <span class="avatar" role="img" aria-label="User profile photo"></span>
      <span class="badge">2</span>
    </header>
    <div class="tile" style="left:28px;top:59px"><svg width="40" height="34" viewBox="0 0 40 34"><path d="M4 30A18 18 0 0 1 36 12" fill="none" stroke="#555" stroke-width="5"/><path d="M20 30L33 8" stroke="#333" stroke-width="2"/></svg>Riskgrid</div>
    <div class="tile" style="left:125px;top:59px"><svg width="36" height="34" viewBox="0 0 36 34"><circle cx="18" cy="17" r="14" fill="none" stroke="#555" stroke-width="4"/><circle cx="18" cy="11" r="3.5" fill="#555"/><path d="M13 26v-7h10v7" fill="#555"/></svg>Simulation</div>
    <div class="tile" style="left:28px;top:140px"><svg width="30" height="36" viewBox="0 0 30 36"><circle cx="15" cy="13" r="10" fill="none" stroke="#555" stroke-width="3"/><circle cx="15" cy="13" r="4" fill="#555"/><path d="M9 22l-3 12 9-5 9 5-3-12" fill="#555"/></svg>Challenges</div>
    <div class="tile" style="left:125px;top:140px"><svg width="30" height="36" viewBox="0 0 30 36"><rect x="4" y="4" width="22" height="30" fill="none" stroke="#555" stroke-width="3"/><path d="M9 12h12M9 18h12M9 24h12" stroke="#555" stroke-width="2"/><rect x="10" y="1" width="10" height="5" fill="#555"/></svg>Booklet</div>
    <div class="tile" style="left:28px;top:224px"><svg width="32" height="34" viewBox="0 0 32 34"><path d="M8 3h16v10a8 8 0 0 1-16 0z" fill="#555"/><path d="M8 6H3c0 6 3 8 5 8M24 6h5c0 6-3 8-5 8" fill="none" stroke="#555" stroke-width="2"/><rect x="14" y="21" width="4" height="6" fill="#555"/><rect x="9" y="27" width="14" height="5" fill="#555"/></svg>Trophies</div>
    <div class="tile" style="left:125px;top:224px"><svg width="34" height="12" viewBox="0 0 34 12"><rect x="1" y="1" width="9" height="9" fill="#444"/><rect x="12.5" y="1" width="9" height="9" fill="#444"/><rect x="24" y="1" width="9" height="9" fill="#444"/></svg>More</div>
    <div class="settings"><svg width="9" height="9" viewBox="0 0 10 10"><circle cx="5" cy="5" r="3" fill="none" stroke="#7aa53a" stroke-width="2.4" stroke-dasharray="2 1"/></svg>CONFIGURAÇÃO</div>
  </section>

  <!-- records -->
  <section class="screen">
    <div class="backdrop soft" role="img" aria-label="Blurred pastel meadow photo"></div>
    <header class="topbar">
      <span class="back"><svg width="10" height="8" viewBox="0 0 10 8"><path d="M1 7V1h6M1 1l7 6" stroke="#333" stroke-width="1.6" fill="none"/></svg></span>
      <span class="user">MARCUS <span>DELVANE</span></span>
      <span class="avatar" role="img" aria-label="User profile photo"></span>
      <span class="badge">2</span>
    </header>
    <h2 class="section green" style="top:28px"><svg width="22" height="22" viewBox="0 0 22 22"><circle cx="11" cy="11" r="9" fill="none" stroke="#fff" stroke-width="2"/><path d="M11 11l5-4" stroke="#fff" stroke-width="2"/></svg>Medidas</h2>
    <div class="record" style="top:78px"><span class="rec-icon"><svg width="14" height="12" viewBox="0 0 14 12"><path d="M3 2h8l2 9H1z" fill="#fff"/></svg>kg</span><span class="rec-value">50<sup>kg</sup></span><span class="rec-date">07.03.2013</span></div>
    <div class="record" style="top:118px"><span class="rec-icon"><svg width="14" height="14" viewBox="0 0 14 14"><path d="M7 1v12M3 1h8M3 13h8" stroke="#fff" stroke-width="1.6"/></svg>cm</span><span class="rec-value">160<sup>cm</sup></span><span class="rec-date">07.03.2013</span></div>
    <h2 class="section orange" style="top:169px"><svg width="22" height="20" viewBox="0 0 22 20"><path d="M1 11h5l2-6 3 11 3-8 2 3h5" fill="none" stroke="#fff" stroke-width="1.8"/></svg>Estilo de vida</h2>
    <div class="record" style="top:219px"><span class="rec-icon"><svg width="14" height="12" viewBox="0 0 14 12"><rect x="5" y="1" width="4" height="8" fill="#fff"/><rect x="2" y="9" width="10" height="2" fill="#fff"/></svg>smoke</span><span class="rec-value">NO</span><span class="rec-date">07.03.2013</span></div>
    <div class="record" style="top:261px"><span class="rec-icon"><svg width="18" height="12" viewBox="0 0 18 12"><circle cx="4" cy="8" r="3" fill="none" stroke="#fff" stroke-width="1.4"/><circle cx="14" cy="8" r="3" fill="none" stroke="#fff" stroke-width="1.4"/><path d="M4 8l4-5 6 5M8 3h3" fill="none" stroke="#fff" stroke-width="1.4"/></svg>activity</span><span class="rec-value">1<sup>per<br>week</sup></span><span class="rec-date">07.03.2013</span></div>
  </section>

  <!-- risk -->
  <section class="screen">
    <div class="backdrop soft" role="img" aria-label="Blurred pastel meadow photo"></div>
    <header class="topbar">
      <span class="back"><svg width="10" height="8" viewBox="0 0 10 8"><path d="M1 7V1h6M1 1l7 6" stroke="#333" stroke-width="1.6" fill="none"/></svg></span>
      <span class="user">MARCUS <span>DELVANE</span></span>
      <span class="avatar" role="img" aria-label="User profile photo"></span>
      <span class="badge">2</span>
    </header>
    <div class="blank"></div>
    <div class="risk-row risk-main"><span class="chev">&gt;</span><svg width="46" height="32" viewBox="0 0 46 32"><path d="M4 26A19 19 0 0 1 40 16" fill="none" stroke="#e4f2cf" stroke-width="5"/><path d="M22 26L34 10" stroke="#e4f2cf" stroke-width="2"/><text x="30" y="31" font-size="11" fill="#fff" font-family="Open Sans,sans-serif">%</text></svg>RISCO</div>
    <div class="risk-row risk-map"><span class="chev">&gt;</span><svg width="28" height="28" viewBox="0 0 28 28"><circle cx="14" cy="14" r="12" fill="none" stroke="#fff" stroke-width="2"/><circle cx="14" cy="8" r="2.5" fill="#fff"/><path d="M11 22v-10h6v10" fill="#fff"/></svg>Mapa do corpo</div>
    <div class="risk-row risk-reduce"><span class="chev" style="color:#fff">&gt;</span><svg width="30" height="22" viewBox="0 0 30 22"><rect x="2" y="8" width="14" height="12" fill="#bbb"/><rect x="14" y="2" width="14" height="12" fill="var(--orange)"/><path d="M17 8l3 3 6-6" fill="none" stroke="#fff" stroke-width="2"/></svg>Reduzir o seu risco</div>
  </section>

</main>
</body>
</html>
```